I'm looking for an app for customers to order through

I'm looking for an app for my customers to order products through
Ideally each customer would have a customer number with password
Their profile would come up with a preloaded products they currently order
From there they can select the product they require and volume needed for delivery
I would also like an option for them to go to a full product range if they are looking for Ideas or a product they don't currently use
Once the order is completed a copy of the order is them e-mailed to my distribution facilities and a confirmation sent to the customer by e-mail and/or SMS
Current product list is approx 1000 items
Current customers is 80 with expectations to expand to 200
On average current products ordered by each customer is is between 4-8 items
Ordering units are done by both weight and pieces/units

Target Market(s)

Food service outlets,
Restaurant , Hotels, catering companies, clubs, take away shops, cafes
Retail outlets

Number of Pages Required

1 page

Font styles to use
Sans Serif

Colors
abd037

Requirements
Must have
• Customer log in with Password 4 - 6 digit
• Customer order history
Nice to have
• Area for promotions / specials on a weekly / monthly basis

```html
<!DOCTYPE html>
<html lang="en">
<head>
<meta charset="utf-8">
<title>Re Order</title>
<link rel="stylesheet" href="https://fonts.googleapis.com/css2?family=Roboto:wght@300;400&display=swap">
<style>
  :root {
    --brand: #abd037;
    --brand-dark: #6a8a22;
    --page-bg: #ececec;
    --card-bg: #ffffff;
    --ink: #1e1e1e;
    --muted: #9a9a9a;
    --tab-bg: #f5f5f5;
    --dot: #b0b0b0;
    --badge-d: #fce68f;
    --badge-m: #f7877a;
    --badge-fav: #d7ec9c;
    --alert: #e02020;
  }
  * { box-sizing: border-box; margin: 0; padding: 0; }
  html, body { width: 675px; height: 1200px; overflow: hidden; }
  body {
    position: relative;
    background: var(--page-bg);
    font-family: "Roboto", "Helvetica Neue", Arial, sans-serif;
    color: var(--ink);
  }
  .app-header { height: 116px; background: var(--brand); color: #fff; position: relative; }
  .status-bar {
    height: 44px; display: flex; align-items: center; justify-content: space-between;
    padding: 0 10px 0 14px; font-size: 18px; font-weight: 400;
  }
  .status-left { display: flex; align-items: center; gap: 6px; }
  .status-right { display: flex; align-items: center; gap: 3px; }
  .screen-title { text-align: center; font-size: 29px; font-weight: 400; margin-top: 10px; }
  .filter-bar {
    height: 79px; background: var(--brand-dark); color: #fff;
    display: flex; align-items: center; justify-content: center; gap: 18px;
    font-size: 28px; font-weight: 300;
  }
  .product-grid { position: absolute; top: 195px; left: 0; width: 675px; height: 919px; overflow: hidden; }
  .product-card {
    position: absolute; width: 316px; background: var(--card-bg);
    padding: 0 7px; display: flex; flex-direction: column;
  }
  .card-top {
    height: 76px; border-bottom: 1.5px solid var(--ink);
    display: flex; align-items: center; gap: 15px; padding-left: 10px; position: relative;
  }
  .tag {
    width: 52px; height: 52px; border-radius: 50%;
    display: flex; align-items: center; justify-content: center;
    font-size: 28px; font-weight: 300; color: var(--ink);
  }
  .tag-d { background: var(--badge-d); }
  .tag-m { background: var(--badge-m); }
  .tag-fav { background: var(--badge-fav); }
  .card-menu { position: absolute; right: 16px; top: 19px; }
  .product-title { font-size: 30px; font-weight: 300; line-height: 36px; margin: 12px 0 10px; }
  .product-photo { height: 128px; width: 298px; }
  .product-desc { font-size: 18px; font-weight: 300; line-height: 22.4px; margin: 12px 2px 0; }
  .reorder-btn {
    width: 200px; height: 61px; margin: 16px auto 22px;
    border: 2px solid var(--brand-dark); color: var(--brand-dark);
    display: flex; align-items: center; justify-content: center;
    font-size: 21px; font-weight: 400;
  }
  .tab-bar {
    position: absolute; left: 0; bottom: 0; width: 675px; height: 86px;
    background: var(--tab-bg); display: flex;
  }
  .tab { flex: 1; display: flex; flex-direction: column; align-items: center; padding-top: 9px; font-size: 18px; }
  .tab-active { color: var(--brand-dark); }
  .tab-idle { color: var(--muted); }
  .tab-label { margin-top: 4px; }
</style>
</head>
<body>
  <header class="app-header">
    <div class="status-bar">
      <div class="status-left">
        <svg width="56" height="10" viewBox="0 0 56 10"><g fill="#fff"><circle cx="5" cy="5" r="4.5"/><circle cx="16" cy="5" r="4.5"/><circle cx="27" cy="5" r="4.5"/><circle cx="38" cy="5" r="4.5"/><circle cx="49" cy="5" r="4.5"/></g></svg>
        <span>Nova</span>
        <svg width="22" height="16" viewBox="0 0 22 16" fill="none" stroke="#fff" stroke-width="2"><path d="M2 6a13 13 0 0 1 18 0"/><path d="M5.5 9.5a8 8 0 0 1 11 0"/><circle cx="11" cy="13.5" r="1.5" fill="#fff"/></svg>
      </div>
      <span>07:29</span>
      <div class="status-right">
        <svg width="44" height="18" viewBox="0 0 44 18"><rect x="1" y="1" width="38" height="16" rx="3" fill="none" stroke="#fff" stroke-width="1.5"/><rect x="3.5" y="3.5" width="33" height="11" rx="1.5" fill="#e6f2c4"/><rect x="40" y="6" width="3" height="6" fill="#fff"/></svg>
        <svg width="10" height="18" viewBox="0 0 10 18"><path d="M6 0L0 10h4l-1 8 7-11H6z" fill="#fff"/></svg>
      </div>
    </div>
    <h1 class="screen-title">Re Order</h1>
  </header>

  <div class="filter-bar">
    <svg width="24" height="24" viewBox="0 0 24 24"><path d="M1 2h22l-8.5 10v10l-5-3v-7z" fill="#fff"/></svg>
    <span>Filter</span>
  </div>

  <main class="product-grid">
    <article class="product-card" style="left:12px; top:11px; height:504px;">
      <div class="card-top">
        <span class="tag tag-d">D</span>
        <span class="tag tag-fav"><svg width="28" height="28" viewBox="0 0 24 24"><path d="M12 1.5l3.1 7.1 7.6.6-5.8 5 1.8 7.5L12 17.7l-6.7 4 1.8-7.5-5.8-5 7.6-.6z" fill="#111"/></svg></span>
        <svg class="card-menu" width="12" height="38" viewBox="0 0 12 38"><g fill="var(--dot)"><circle cx="6" cy="5" r="5"/><circle cx="6" cy="19" r="5"/><circle cx="6" cy="33" r="5"/></g></svg>
      </div>
      <h2 class="product-title">Product Title</h2>
      <div class="product-photo" role="img" aria-label="Assorted cheese wedges on a board" style="background:linear-gradient(110deg,#6b6a62 0%,#c8761f 25%,#e8c25a 45%,#efdc9a 65%,#c9b690 85%,#707068 100%);"></div>
      <p class="product-desc">Product Description Vestibulum turpis sem, aliquet eget, lobortis pellentesque, rutrum eu, nisl. Sed fringilla mauris sit amet nibh. Phasellus nec sem in justo pellen-tesque facilisis.</p>
      <div class="reorder-btn">Re-Order</div>
    </article>

    <article class="product-card" style="left:346px; top:11px; height:506px;">
      <div class="card-top">
        <span class="tag tag-m">M</span>
        <span class="tag tag-fav"><svg width="28" height="28" viewBox="0 0 24 24"><path d="M12 1.5l3.1 7.1 7.6.6-5.8 5 1.8 7.5L12 17.7l-6.7 4 1.8-7.5-5.8-5 7.6-.6z" fill="#111"/></svg></span>
        <svg class="card-menu" width="12" height="38" viewBox="0 0 12 38"><g fill="var(--dot)"><circle cx="6" cy="5" r="5"/><circle cx="6" cy="19" r="5"/><circle cx="6" cy="33" r="5"/></g></svg>
      </div>
      <h2 class="product-title">Second Product Title</h2>
      <div class="product-photo" role="img" aria-label="Marbled raw beef cuts on a wooden board" style="background:linear-gradient(160deg,#b2495a 0%,#e8aab2 40%,#d98a96 60%,#a05a3a 85%,#7a4a2a 100%);"></div>
      <p class="product-desc">Product Description Vestibulum turpis sem, aliquet eget, lobortis pellentesque, rutrum eu, nisl. Sed fringilla mauris sit amet nibh.</p>
      <div class="reorder-btn" style="margin-top:58px;">Re-Order</div>
    </article>

    <article class="product-card" style="left:12px; top:525px; height:420px;">
      <div class="card-top">
        <span class="tag tag-m">M</span>
        <svg class="card-menu" width="12" height="38" viewBox="0 0 12 38"><g fill="var(--dot)"><circle cx="6" cy="5" r="5"/><circle cx="6" cy="19" r="5"/><circle cx="6" cy="33" r="5"/></g></svg>
      </div>
      <h2 class="product-title" style="margin-left:5px;">Longer Third Product Title</h2>
      <div class="product-photo" role="img" aria-label="Cured ham leg on a carving stand" style="background:linear-gradient(165deg,#2a1c1c 0%,#b4485a 35%,#d9707e 55%,#8a3a2e 80%,#3a2420 100%);"></div>
      <p class="product-desc">Product Description Vestibulum turpis sem, aliquet eget, lobortis pellentesque, rutrum eu, nisl. Sed fringilla mauris sit amet nibh.</p>
    </article>

    <article class="product-card" style="left:344px; top:525px; height:420px;">
      <div class="card-top">
        <span class="tag tag-m">M</span>
        <svg class="card-menu" width="12" height="38" viewBox="0 0 12 38"><g fill="var(--dot)"><circle cx="6" cy="5" r="5"/><circle cx="6" cy="19" r="5"/><circle cx="6" cy="33" r="5"/></g></svg>
      </div>
      <h2 class="product-title" style="margin-bottom:6px;">FourthProduct Title</h2>
      <div class="product-photo" role="img" aria-label="Braised meat on mash with sauce on a white plate" style="background:radial-gradient(ellipse at 45% 50%,#4a2414 0%,#7a3c20 30%,#d8c8a8 55%,#f2f0ea 80%,#e8e6e0 100%);"></div>
      <p class="product-desc">Product Description Vestibulum turpis sem, aliquet eget, lobortis pellentesque, rutrum eu, nisl. Sed fringilla mauris sit amet nibh.</p>
      <div class="reorder-btn" style="margin-top:20px;">Re-Order</div>
    </article>
  </main>

  <nav class="tab-bar">
    <div class="tab tab-active">
      <svg width="46" height="46" viewBox="0 0 46 46" fill="none" stroke="var(--brand-dark)" stroke-width="2"><circle cx="23" cy="23" r="21.5"/><path d="M12 15h4l3 12h12l2.5-8H17.5" stroke-linejoin="round"/><circle cx="20.5" cy="31" r="1.6"/><circle cx="29.5" cy="31" r="1.6"/></svg>
      <span class="tab-label">My Orders</span>
    </div>
    <div class="tab tab-idle">
      <svg width="50" height="46" viewBox="0 0 50 46" fill="none" stroke="#8a8a8a" stroke-width="2"><circle cx="23" cy="23" r="21.5"/><path d="M18.5 27c-2.5-2-3.5-4-3.5-6.5a8 8 0 0 1 16 0c0 2.5-1 4.5-3.5 6.5v3h-9z"/><path d="M19 33h8M20 36h6"/><circle cx="41" cy="8" r="8" fill="var(--alert)" stroke="none"/><text x="41" y="12.5" font-size="12" fill="#fff" stroke="none" text-anchor="middle" font-family="Roboto, sans-serif">1</text></svg>
      <span class="tab-label">Find Something New</span>
    </div>
  </nav>
</body>
</html>
```